Business Card Design Project

Colette Marivaux logo on front of card with 'of Sydney' added in small font.
Back of card needs to include the following information :

"Pure pleasure for the discerning gentleman" (I may omit once I've seen the design)

colettemarivaux.com.au

Contact by SMS or email only :

colette@colettemarivaux.com.au
Mobile : 0483 956 204 or + 61 483 956 204

Target Market(s)

Male professionals aged 20-60.

Industry/Entity Type

Business

Requirements
Must have
• Simple, bold, stylish and elegant.

```html
<!DOCTYPE html>
<html lang="en">
<head>
<meta charset="utf-8">
<title>Colette Marivaux of Sydney — Business Card</title>
<link rel="stylesheet" href="https://fonts.googleapis.com/css2?family=Open+Sans:wght@400;600&family=Pinyon+Script&display=swap">
<style>
  :root {
    --stage: #2a2a2a;
    --card: #0b0809;
    --card-edge: #1a1718;
    --ink-light: #f2eee6;
    --ink-soft: #cfcac2;
    --silver: #d9d9d9;
  }
  * { box-sizing: border-box; margin: 0; padding: 0; }
  html, body {
    width: 1200px;
    height: 900px;
    overflow: hidden;
    background: var(--stage);
  }
  .canvas {
    position: relative;
    width: 1200px;
    height: 900px;
  }
  .card {
    position: absolute;
    width: 560px;
    height: 320px;
    background: var(--card);
    border: 1px solid var(--card-edge);
    box-shadow: 0 18px 40px rgba(0, 0, 0, 0.55);
    overflow: hidden;
  }
  .card--back { left: 70px; top: 110px; }
  .card--front { left: 570px; top: 470px; }

  .back-content {
    position: absolute;
    inset: 0;
    display: flex;
    flex-direction: column;
    align-items: center;
    justify-content: center;
    text-align: center;
    color: var(--ink-soft);
    font-family: "Open Sans", sans-serif;
  }
  .tagline {
    font-family: "Pinyon Script", cursive;
    font-size: 25px;
    color: var(--ink-light);
    margin-bottom: 6px;
  }
  .contact-line {
    font-size: 11px;
    line-height: 1.35;
    letter-spacing: 0.3px;
  }
  .contact-line--small { font-size: 9px; }
  .ornament-spot {
    display: block;
    width: 8px;
    height: 8px;
    margin-top: 6px;
    border-radius: 50%;
    background: var(--ink-soft);
  }

  .brand {
    position: absolute;
    right: 38px;
    top: 120px;
    text-align: right;
    font-family: "Open Sans", sans-serif;
    font-weight: 400;
    color: var(--silver);
    font-size: 24px;
    letter-spacing: 3px;
    text-transform: uppercase;
    line-height: 1.25;
  }
</style>
</head>
<body>
<main class="canvas">
  <section class="card card--back" aria-label="Back of business card">
    <div class="back-content">
      <p class="tagline">“Pure pleasure for the discerning gentleman”</p>
      <p class="contact-line">colettemarivaux.com.au</p>
      <p class="contact-line">Contact by SMS or email only :</p>
      <p class="contact-line">colette@colettemarivaux.com.au</p>
      <p class="contact-line contact-line--small">Mobile : 0483 956 204 or + 61 483 956 204</p>
      <span class="ornament-spot" role="img" aria-label="Small decorative flourish"></span>
    </div>
  </section>

  <section class="card card--front" aria-label="Front of business card">
    <p class="brand">Colette Marivaux<br>of Sydney</p>
  </section>
</main>
</body>
</html>
```